Roadside building business signage for a holistic health clinic.

Replace signs as shown in the attached file. They are perforated stickers that go on the windows as shown. Looking for something that has our logo and says the name of the practice with logo (Fernbrook Health & Wellness) also boldly says Acupuncture, IV Vitamins, and Holistic Health.
Possibly our phone number as well 318-627-5194
Updates

Please don't use pink except the logo. Earthy, organic tone colors appreciated.

Need of eye catching window signage of a holistic clinic on a brick building. Pink, purple, sage green, white color. Logo is pink on a white background. Please don't overload with too much pink. Words to include are "Fernbrook Health and Wellness(name of business)", "Direct Primary Care", " Medical acupuncture", "IV Vitamin Therapy", "fernbrookcare-example.com","318-627-5194".

Target Market(s)

People will see in their cars passing by the building. Busy roadside so need to be visible while passing in fast speed.

Industry/Entity Type

Health & Wellness

Font styles to use
Sans Serif

Colors

Designer to choose colors to be used in the design.

Requirements
Must have
• On sign must have words Holistic Medicine, Medical Acupuncture, Direct Primary Care and IV vitamins.
Nice to have
• Simple, minimalistic, artistic yet has clear message. White, Black, Violet, Pink (logo), Dark green, Sage green.
Should not have
• Bold colors (red, yellow, blue), same tone colors. Blue waves on the current signage (uploaded file) must go.

```html
<!DOCTYPE html>
<html lang="en">
<head>
<meta charset="utf-8">
<title>Fernbrook Health &amp; Wellness — Window Panels</title>
<link href="https://fonts.googleapis.com/css2?family=Oswald:wght@500&family=Roboto+Condensed:wght@400;500;700&display=swap" rel="stylesheet">
<style>
  :root{
    --backdrop:#9c9c9c;
    --panel:#ece9e0;
    --forest:#23483a;
    --sage:#6f8a66;
    --violet:#6a4c8a;
    --logo-rose:#e3287a;
    --citrus:#e98a2a;
    --leaf:#6f9a3a;
    --portrait-dark:#4a3a30;
    --portrait-light:#b6a08a;
  }
  *{box-sizing:border-box;margin:0;padding:0}
  html,body{width:1200px;height:515px;overflow:hidden;background:var(--backdrop)}
  .window-set{position:absolute;left:222px;top:32px;width:757px;height:451px}
  .panel{position:absolute;width:144px;height:144px;background:var(--panel);
    display:flex;flex-direction:column;align-items:center;justify-content:center;text-align:center;
    font-family:"Roboto Condensed",sans-serif;overflow:hidden;padding:0 6px}
  .arch-left{border-top-left-radius:100% 100%}
  .arch-right{border-top-right-radius:100% 100%}
  .brand{justify-content:flex-end;padding-bottom:30px}
  .brand-dot{width:26px;height:26px;border-radius:50%;background:var(--logo-rose);margin-bottom:8px}
  .brand-name{color:var(--forest);font-weight:500;font-size:20px;letter-spacing:3px;line-height:1}
  .brand-sub{color:var(--forest);font-weight:500;font-size:6px;letter-spacing:1.6px;margin-top:3px}
  .practice-name{color:var(--violet);font-weight:500;font-size:21px;line-height:1.05}
  .care-line{color:var(--sage);font-weight:700;font-size:12px;letter-spacing:.6px;margin-top:6px;text-transform:uppercase}
  .call-label{color:var(--sage);font-weight:700;font-size:16px}
  .phone{font-family:"Oswald",sans-serif;color:var(--forest);font-weight:500;font-size:25px;line-height:1.15}
  .web{color:var(--forest);font-weight:500;font-size:11.5px}
  .service{color:var(--forest);line-height:1}
  .service-icon{width:38px;height:38px;margin-bottom:6px;fill:none;stroke:var(--violet);stroke-width:2.2;stroke-linecap:round;stroke-linejoin:round}
  .holistic{font-weight:500;font-size:24px}
  .acu-main{font-weight:700;font-size:26px}
  .acu-sub{font-weight:500;font-size:14px;margin-top:1px}
  .vitamin{font-weight:500;font-size:22px}
  .produce{background:radial-gradient(circle at 35% 35%,var(--citrus),#c9a23a 45%,var(--leaf) 80%)}
  .portrait{background:linear-gradient(160deg,var(--portrait-light),var(--portrait-dark))}
</style>
</head>
<body>
<main class="window-set">
  <section class="panel arch-left brand" style="left:304px;top:0">
    <span class="brand-dot"></span>
    <span class="brand-name">FERNBROOK</span>
    <span class="brand-sub">HEALTH &amp; WELLNESS</span>
  </section>
  <section class="panel arch-right brand" style="left:458px;top:0">
    <span class="brand-dot"></span>
    <span class="brand-name">FERNBROOK</span>
    <span class="brand-sub">HEALTH &amp; WELLNESS</span>
  </section>

  <section class="panel" style="left:151px;top:153px">
    <p class="call-label">Call Today</p>
    <p class="phone">318-627-5194</p>
    <p class="web">fernbrookcare-example.com</p>
  </section>
  <section class="panel" style="left:304px;top:153px">
    <p class="practice-name">Fernbrook<br>Health and<br>Wellness</p>
  </section>
  <section class="panel" style="left:458px;top:153px">
    <p class="practice-name">Fernbrook<br>Health and<br>Wellness</p>
    <p class="care-line">Direct Primary Care</p>
  </section>
  <div class="panel produce" style="left:613px;top:153px" role="img" aria-label="Photo of fresh fruit and vegetables: oranges, kiwi, tomatoes and greens"></div>

  <section class="panel" style="left:0;top:306px">
    <svg class="service-icon" viewBox="0 0 40 40" aria-hidden="true">
      <circle cx="20" cy="20" r="4"/>
      <circle cx="20" cy="9" r="6"/><circle cx="20" cy="31" r="6"/>
      <circle cx="9.5" cy="14.5" r="6"/><circle cx="30.5" cy="14.5" r="6"/>
      <circle cx="9.5" cy="25.5" r="6"/><circle cx="30.5" cy="25.5" r="6"/>
    </svg>
    <p class="service holistic">HOLISTIC<br>HEALTH</p>
  </section>
  <section class="panel" style="left:151px;top:306px">
    <svg class="service-icon" viewBox="0 0 40 40" aria-hidden="true">
      <circle cx="20" cy="6" r="3.5"/>
      <path d="M6 14h28M20 14v10M15 38l5-14 5 14"/>
    </svg>
    <p class="service acu-main">MEDICAL</p>
    <p class="service acu-sub">ACUPUNCTURE</p>
  </section>
  <section class="panel" style="left:304px;top:306px">
    <svg class="service-icon" viewBox="0 0 40 40" aria-hidden="true">
      <path d="M27 5l8 8M31 9l-4 4M29 11L13 27l-4-4L25 7zM11 25l-7 7M16 16l3 3M20 12l3 3"/>
    </svg>
    <p class="service vitamin">IV VITAMIN<br>THERAPY</p>
  </section>
  <div class="panel portrait" style="left:458px;top:306px" role="img" aria-label="Photo of a smiling woman with long dark hair outdoors"></div>
  <section class="panel" style="left:613px;top:306px">
    <p class="call-label">Call Today</p>
    <p class="phone">318-627-5194</p>
    <p class="web">fernbrookcare-example.com</p>
  </section>
</main>
</body>
</html>
```